Company brochure

I would like to redesign our existing brochure.
It shall be trifold brochure with more modern and better appealing design than the old one. I am uploading the old one. The new design shall have all all information repeated from old brochure. It could be more or less pictures. I will provide more pictures if required. The keep text is important, the font shall be more modern. Brochure size shall be trifoldt US Legal size paper 8.5" x 14". I will provide all pitures, logos etc in a original format after design concept will be established or before on request.

Industry/Entity Type

It Company

Font styles to use
Other font styles liked:
• calibri

Colors
0555a3
3176b5
85abd2
0692cd
33a6d7
85cae6
1ab09a
33b8a4
87cfc6

Requirements
Nice to have
• I need all information from existing brochure such as text, customer logos, professional assos. logos to be shown in a new one. Picture could be added more.
Should not have
• No changes allowed to company letterhead. Only slight modifications allowed to company logo

```html
<!DOCTYPE html>
<html lang="en">
<head>
<meta charset="utf-8">
<title>Polar Crest Refrigeration &amp; Air Conditioning – Trifold Brochure</title>
<link href="https://fonts.googleapis.com/css2?family=Oswald:wght@600&family=Questrial&display=swap" rel="stylesheet">
<style>
:root{
  --navy:#0a2f6e;
  --blue:#0555a3;
  --teal:#2fd0b5;
  --teal-dark:#1ab09a;
  --teal-soft:#87cfc6;
  --ink:#2a2a2a;
  --paper:#ffffff;
  --mist:#e9eef2;
  --stage:#d9dde1;
}
*{box-sizing:border-box;margin:0;padding:0}
html,body{width:756px;height:1200px;overflow:hidden;background:var(--stage)}
body{position:relative;font-family:"Questrial",sans-serif;color:var(--ink)}
.brochure{position:absolute;left:18px;top:382px;width:720px;height:436px;background:var(--paper);overflow:hidden;box-shadow:0 6px 24px rgba(0,0,0,.18)}
.panel{position:absolute;top:0;height:436px;width:240px}
.panel--services{left:0;background:linear-gradient(#fafbfc,#eef1f3)}
.panel--contact{left:240px;background:linear-gradient(#f3f6f8,#e4eaef)}
.panel--cover{left:480px;background:linear-gradient(#f2f5f8,#e6ecf1)}
.pill{position:absolute;left:20px;width:191px;background:var(--teal);color:#fff;border-radius:14px;text-align:center;font-size:11.5px;line-height:14px;padding:3px 6px}
.copy{position:absolute;left:10px;width:220px;font-size:7.6px;line-height:10.2px;text-align:justify;text-align-last:center}
.photo-round{position:absolute;left:59px;top:23px;width:120px;height:120px;border-radius:50%;border:4px solid var(--teal);background:radial-gradient(circle at 40% 40%,#9fb7c6,#4d6677 70%,#3a4d58)}
.wordmark{font-family:"Oswald",sans-serif;font-weight:600;color:var(--navy);text-transform:uppercase;letter-spacing:.2px}
.panel--contact .wordmark{position:absolute;left:20px;top:165px;width:200px;font-size:13.5px;line-height:16px;text-align:center}
.address{position:absolute;left:0;top:222px;width:240px;text-align:center;font-size:10.4px;line-height:14.6px}
.address .lic{font-weight:700}
.badges{position:absolute;left:10px;top:330px;width:220px;display:flex;justify-content:space-around}
.badge{width:34px;height:34px;background:#fff;border:2px solid var(--blue)}
.badge--round{border-radius:50%}
.panel--cover .wordmark{position:absolute;left:20px;top:24px;width:210px;font-size:15px;line-height:18px;text-align:center}
.tagline{position:absolute;top:98px;font-size:7.4px;line-height:12px}
.tagline--left{left:10px}
.tagline--right{left:153px}
.cover-dot{position:absolute;left:122px;top:98px;width:22px;height:22px;border-radius:50%;background:var(--teal)}
.photo-plant{position:absolute;left:0;top:150px;width:240px;height:240px;background:linear-gradient(160deg,#dfe5ea 0%,#a9b9c3 35%,#5c7482 70%,#394b56 100%)}
.wave{position:absolute;left:0;bottom:0;width:720px;height:120px}
.url{position:absolute;left:480px;bottom:14px;width:240px;text-align:center;color:#fff;font-weight:700;font-size:11px;letter-spacing:.3px}
</style>
</head>
<body>
<main class="brochure">
  <section class="panel panel--services">
    <div class="pill" style="top:22px">Refrigeration Facilities Serviced</div>
    <p class="copy" style="top:52px">Food processing, cold storages and distribution facilities, meat and poultry processing plants, bakeries, dairies, beverage bottling facilities, ice production, chemical plants, refineries and ice rinks.</p>
    <div class="pill" style="top:106px">Industrial &amp; Commercial<br>HVAC Facilities Serviced</div>
    <p class="copy" style="top:155px">Production plant and manufacturing facilities, distribution and storage warehouses, office buildings, data centers, hospitals, colleges, shopping malls and country clubs.</p>
    <div class="pill" style="top:199px">Construction</div>
    <p class="copy" style="top:231px">Ammonia and freon refrigeration build-up systems. Refrigeration and HVAC equipment changeover. Freon packaged condensing units and chillers. Blast freezers, spiral and tunnel freezers. Computerized control, control and power wiring. Build-up glycol and water chillers. Air handlers and evaporators. Refrigeration, glycol, chill water and process piping. Certified X-ray quality welding. Carbon steel, stainless steel, copper, PVC and sanitary piping. Hot tapping available.</p>
  </section>

  <section class="panel panel--contact">
    <div class="photo-round" role="img" aria-label="Photo of an industrial compressor unit with blue piping"></div>
    <div class="wordmark">Polar Crest Refrigeration<br>&amp; Air Conditioning</div>
    <p class="address">4180 Harbor Ridge Avenue<br>Lakeview Park, CA 90412<br>555-201-4470<br>555-201-4471<br>www.polarcrestinc.com<br><span class="lic">Lic. # 742315</span></p>
    <div class="badges">
      <div class="badge" role="img" aria-label="Customer badge"></div>
      <div class="badge" role="img" aria-label="Professional association badge"></div>
      <div class="badge badge--round" role="img" aria-label="Professional association badge"></div>
      <div class="badge badge--round" role="img" aria-label="Professional association badge"></div>
    </div>
  </section>

  <section class="panel panel--cover">
    <div class="wordmark">Polar Crest Refrigeration<br>&amp; Air Conditioning</div>
    <p class="tagline tagline--left">Industrial &amp; Commercial<br>Ammonia &amp; Freon<br>Service &amp; Maintenance</p>
    <div class="cover-dot"></div>
    <p class="tagline tagline--right">Design &amp; Engineering<br>Construction</p>
    <div class="photo-plant" role="img" aria-label="Photo of an industrial refrigeration plant room with compressors and yellow piping"></div>
  </section>

  <svg class="wave" viewBox="0 0 720 120" preserveAspectRatio="none" aria-hidden="true">
    <defs>
      <linearGradient id="tealFill" x1="0" y1="0" x2="0" y2="1">
        <stop offset="0" stop-color="#2fd0b5"/>
        <stop offset="1" stop-color="#1ab09a"/>
      </linearGradient>
    </defs>
    <path d="M0,20 C160,40 300,95 480,70 C580,56 660,40 720,30 L720,120 L0,120 Z" fill="#87cfc6" opacity=".55"/>
    <path d="M0,30 C170,55 320,108 480,82 C580,66 660,52 720,44 L720,120 L0,120 Z" fill="url(#tealFill)"/>
    <path d="M0,40 C180,68 330,112 480,92 C590,78 660,64 720,58" fill="none" stroke="#fff" stroke-width="2" opacity=".7"/>
  </svg>
  <div class="url">www.polarcrestinc.com</div>
</main>
</body>
</html>
```